Natural Medicine & Health/Fitness Coaching studio requires web page

Require a innovative web page for a studio that coaches clients to better health, nutrition and fitness. The studio compromises of Clinical Nutritionists, Naturopaths, Rehab Trainers, Personal Trainers and Sport Coaches. Would like to see earthy but bold designs emphasizing nutritional health and athletic performance.
Updates

Design only launched today.

Target Market(s)

All genders from 20's to 60's, as well as families

Industry/Entity Type

Nutritionist

Coding

Coded - Design and coding required

Number of Pages Required

3 page

Colors
abd037
3277b5
fbee3d
fece3e
33b8a4
f04a50

Requirements
Must have
• Online booking system, ability to message
• Home page
• Coaching/Fitness page
• Nutritional Medicine page
• Must be suitable for both Fitness and Nutrition

```html
<!DOCTYPE html>
<html lang="en">
<head>
<meta charset="utf-8">
<title>Verdant Fit – Nutrition &amp; Fitness Coaching</title>
<link href="https://fonts.googleapis.com/css2?family=Raleway:wght@300;400;600;700&display=swap" rel="stylesheet">
<style>
:root{
  --lime:#a3c429;
  --lime-dark:#8fb01e;
  --yellow:#fbe800;
  --ink:#222;
  --muted:#666;
  --backdrop:#efefef;
  --paper:#ffffff;
  --night:#0d0d0d;
}
*{margin:0;padding:0;box-sizing:border-box}
html,body{width:1200px;height:1200px;overflow:hidden;background:var(--backdrop);font-family:"Raleway",sans-serif;color:var(--ink)}
.stage{position:absolute;left:0;top:0;width:1500px;height:1500px;transform:scale(.8);transform-origin:0 0}
.page{position:absolute;left:551px;top:0;width:400px;height:1500px;background:var(--paper);overflow:hidden}
.abs{position:absolute}
.center{left:0;width:400px;text-align:center}
.label{font-size:5px;color:var(--lime);font-weight:600;line-height:6px}
.rule{position:absolute;left:192px;width:16px;height:0.6px;background:var(--lime)}
.title{font-size:9px;font-weight:300;color:#333;line-height:11px}
.small{font-size:3.8px;line-height:6.2px;color:var(--muted)}
.btn{position:absolute;background:var(--yellow);border-radius:8px;font-size:3.8px;font-weight:700;color:#222;display:flex;align-items:center;justify-content:center}
.photo{position:absolute}
.topbar{top:0;left:0;width:400px;height:15px;background:var(--night);color:#fff;font-size:3.8px;display:flex;align-items:center}
.topbar .contact{position:absolute;left:55px;display:flex;gap:5px;align-items:center}
.topbar .socials{position:absolute;right:55px;display:flex;gap:4px}
.dot{width:3px;height:3px;border-radius:50%;background:var(--lime);display:inline-block}
.brand{font-weight:400;color:var(--lime-dark);font-size:9px}
.header-logo{left:50px;top:15px;width:95px;height:27px;background:#fff;clip-path:polygon(0 0,100% 0,88% 100%,0 100%);display:flex;align-items:center;padding-left:5px;gap:3px}
.nav{left:135px;top:15px;width:215px;height:27px;background:var(--lime);display:flex;justify-content:flex-end;align-items:center;gap:10px;padding-right:5px;font-size:3.8px;color:#fff;clip-path:polygon(8% 0,100% 0,100% 100%,0 100%)}
.hero{top:15px;left:0;width:400px;height:205px;background:
  radial-gradient(ellipse 120px 70px at 250px 80px,rgba(190,210,120,.55),transparent 70%),
  radial-gradient(ellipse 90px 60px at 330px 120px,rgba(120,150,70,.5),transparent 70%),
  linear-gradient(180deg,#1f2a17 0%,#4e6a2e 35%,#6f8c44 55%,#4a5a30 78%,#2a2c22 100%)}
.hero-kicker{left:49px;top:96px;font-size:5px;color:var(--lime)}
.hero-title{left:49px;top:106px;font-size:14.5px;color:#fff;font-weight:400;line-height:18px}
.about{top:220px;left:0;width:400px;height:267px;background:
  radial-gradient(ellipse 140px 120px at 200px 140px,rgba(225,205,195,.55),transparent 70%),
  linear-gradient(135deg,#f6f4f0,#ece6df 50%,#f4f3ef)}
.card{position:absolute;top:297px;width:125px;height:169px;background:#fff;box-shadow:0 1px 4px rgba(0,0,0,.15)}
.card .img{position:absolute;left:0;top:0;width:125px;height:97px}
.card h3{position:absolute;top:105px;width:125px;text-align:center;font-size:7px;font-weight:400;color:var(--lime)}
.card p{position:absolute;top:118px;left:13px;width:99px;text-align:center}
.service{top:487px;left:0;width:400px;height:170px;background:var(--lime)}
.svc{position:absolute;top:560px;width:74px;text-align:center}
.svc .ring{width:24px;height:24px;margin:0 auto;border:0.8px solid #fff;border-radius:50%;display:flex;align-items:center;justify-content:center}
.svc h4{margin-top:8px;font-size:3.9px;font-weight:700;color:#222}
.svc p{margin-top:3px;font-size:3.6px;line-height:5.8px;color:#fff}
.testimonial{top:995px;left:0;width:400px;height:117px;background:
  radial-gradient(ellipse 220px 40px at 200px 60px,rgba(120,150,40,.45),transparent 70%),
  linear-gradient(180deg,#9cc12e,#a4c43a 60%,#93b827)}
.quote-box{left:95px;top:1034px;width:210px;height:45px;border:0.8px solid rgba(255,255,255,.75);padding:6px 8px}
.avatar{left:189px;top:1068px;width:23px;height:23px;border-radius:50%;background:#d9d2c6;border:1.5px solid #fff}
.contact-sec{top:1134px;left:0;width:400px;height:196px;background:
  radial-gradient(ellipse 50px 60px at 20px 120px,rgba(150,110,80,.35),transparent 70%),
  linear-gradient(90deg,#e6e4de,#f5f4f1 40%,#f2f1ee)}
.form{left:74px;top:1209px;width:252px;height:99px;background:#fff;box-shadow:0 1px 4px rgba(0,0,0,.12)}
.field{position:absolute;font-size:3.6px;color:#999;border-bottom:0.6px solid #ddd;padding-bottom:3px}
.footer{top:1330px;left:0;width:400px;height:170px;background:#fff}
.foot-deco{left:50px;top:1352px;width:300px;height:140px;background:
  radial-gradient(ellipse 40px 70px at 30px 70px,rgba(230,180,140,.25),transparent 70%),
  radial-gradient(ellipse 40px 70px at 270px 60px,rgba(230,180,140,.25),transparent 70%),
  linear-gradient(180deg,rgba(236,232,220,.35),rgba(245,242,236,.15))}
.badge{position:absolute;top:1448px;height:11px;background:#1f4f8f}
</style>
</head>
<body>
<div class="stage">
<main class="page">

  <div class="abs topbar">
    <div class="contact">
      <svg width="4" height="4" viewBox="0 0 10 10"><path d="M2 1l2 0 1 2-1 1.5c.6 1.2 1.3 1.9 2.5 2.5L8 5l2 1v2c-4.5 0-8-3.5-8-7z" fill="#a3c429"/></svg>
      <span>+1 202-555-0147</span>
      <svg width="5" height="4" viewBox="0 0 10 8"><rect x="0.5" y="0.5" width="9" height="7" fill="none" stroke="#a3c429"/><path d="M.5 .5l4.5 4 4.5-4" fill="none" stroke="#a3c429"/></svg>
      <span>hello@verdantfit.example</span>
    </div>
    <div class="socials"><span class="dot"></span><span class="dot"></span><span class="dot"></span><span class="dot"></span><span class="dot" style="background:none;border:0.6px solid #a3c429;margin-left:4px"></span></div>
  </div>

  <div class="abs hero" role="img" aria-label="Photo of a group doing outdoor yoga with arms outstretched in a green park"></div>
  <div class="abs header-logo"><span class="dot" style="width:5px;height:5px"></span><span class="brand">Verdant Fit</span></div>
  <nav class="abs nav"><span>Home</span><span>About</span><span>Service</span><span>Gallery</span><span>Contact Us</span></nav>
  <div class="abs hero-kicker">Lifestyle &amp; dietary habits</div>
  <h1 class="abs hero-title">Healthy liver<br>Gallbladder functions</h1>
  <div class="btn" style="left:49px;top:150px;width:46px;height:14px">BOOK NOW</div>

  <section class="abs about" role="img" aria-label="Faint background photo of a woman in a knit sweater"></section>
  <div class="abs center label" style="top:240px">About Us</div>
  <div class="rule" style="top:248px"></div>
  <h2 class="abs center title" style="top:251px">Eat right for healthy digestion</h2>
  <p class="abs center small" style="top:266px;left:115px;width:170px">We all know that healthy eating is important. The Mediterranean style of eating is possibly the most healthful</p>

  <article class="card" style="left:60px">
    <div class="img" role="img" aria-label="Photo of a white bowl of fresh salad with a fork" style="background:radial-gradient(ellipse 40px 22px at 60px 42px,rgba(140,180,90,.55),transparent 70%),linear-gradient(180deg,#f0f0ee,#dcdbd7)"></div>
    <h3>Healthy liver</h3>
    <p class="small">We all know that healthy eating is important. The Mediterranean style of eating is possibly the most healthful and so</p>
    <div class="btn" style="left:43px;top:144px;width:39px;height:13px">Read More</div>
  </article>
  <article class="card" style="left:215px">
    <div class="img" role="img" aria-label="Photo of a woman stretching on a rooftop in front of city towers" style="height:95px;background:linear-gradient(180deg,#d5dde6,#aab5c0 55%,#8a7a7e 85%,#6d6a6b)"></div>
    <h3>Gallbladder functions</h3>
    <p class="small">We all know that healthy eating is important. The Mediterranean style of eating is possibly the most healthful and so</p>
    <div class="btn" style="left:43px;top:144px;width:39px;height:13px">Read More</div>
  </article>

  <section class="abs service"></section>
  <div class="abs center label" style="top:507px;color:#222">Service</div>
  <div class="rule" style="top:515px;background:#fff"></div>
  <h2 class="abs center title" style="top:518px">Don't sweat the small stuff</h2>
  <p class="abs center small" style="top:533px;left:130px;width:140px;color:#fff">We all know that healthy eating is important. The Mediterranean possibly most healthful</p>

  <div class="svc" style="left:44px">
    <div class="ring"><svg width="11" height="11" viewBox="0 0 12 12" fill="none" stroke="#fff" stroke-width=".8"><circle cx="6" cy="2.5" r="1.5"/><path d="M6 4v4M3 11l3-3 3 3M3 6h6"/></svg></div>
    <h4>NUTRITIONISTS</h4><p>Balanced meals, fresh plates, and plans for anything else you need</p>
  </div>
  <div class="svc" style="left:123px">
    <div class="ring"><svg width="11" height="11" viewBox="0 0 12 12" fill="none" stroke="#fff" stroke-width=".8"><path d="M2 9l8-6M3 4l6 6M2 6h3"/></svg></div>
    <h4>REHAB TRAINERS</h4><p>Gentle recovery, mobility work, and care for anything else you need</p>
  </div>
  <div class="svc" style="left:203px">
    <div class="ring"><svg width="11" height="11" viewBox="0 0 12 12" fill="none" stroke="#fff" stroke-width=".8"><circle cx="6" cy="3" r="1.6"/><path d="M2 5l4 1.5L10 5M6 6.5V11M4 11h4"/></svg></div>
    <h4>PERSONAL TRAINERS</h4><p>Strength sessions, tailored routines, and goals for anything you want</p>
  </div>
  <div class="svc" style="left:282px">
    <div class="ring"><svg width="11" height="11" viewBox="0 0 12 12" fill="none" stroke="#fff" stroke-width=".8"><circle cx="8" cy="2.5" r="1.3"/><path d="M2 10l3-3 2 1 1-3-3-1M7 8l1 3"/></svg></div>
    <h4>SPORT COACHES</h4><p>Speed drills, match prep, and coaching for any sport you choose</p>
  </div>
  <div class="btn" style="left:181px;top:624px;width:38px;height:12px">Read More</div>

  <div class="abs center label" style="top:677px">Gallery</div>
  <div class="rule" style="top:685px"></div>
  <h2 class="abs center title" style="top:688px">Make the for doing things you love</h2>
  <p class="abs center small" style="top:703px;left:130px;width:140px">We all know that healthy eating is important. The Mediterranean possibly most healthful</p>

  <div class="photo" role="img" aria-label="Photo of an athlete jumping against a white wall" style="left:50px;top:733px;width:95px;height:111px;background:radial-gradient(ellipse 14px 40px at 48px 55px,rgba(60,60,70,.35),transparent 70%),linear-gradient(180deg,#f4f4f4,#d7d8dc)"></div>
  <div class="photo" role="img" aria-label="Photo of a barbell deadlift in a gym" style="left:50px;top:863px;width:95px;height:51px;background:linear-gradient(180deg,#3d3a34,#7a6a4c 55%,#2b2a27)"></div>
  <div class="photo" role="img" aria-label="Photo of a woman exercising on a gym floor" style="left:50px;top:922px;width:95px;height:51px;background:radial-gradient(ellipse 16px 18px at 48px 26px,rgba(200,70,90,.45),transparent 70%),linear-gradient(180deg,#8a8683,#c8b7b9 60%,#6a6666)"></div>
  <div class="photo" role="img" aria-label="Photo of a suspension strap workout in a gym" style="left:153px;top:733px;width:95px;height:64px;background:radial-gradient(ellipse 40px 10px at 48px 42px,rgba(190,60,50,.45),transparent 70%),linear-gradient(180deg,#2a2a2a,#5a4a40 55%,#1d1d1d)"></div>
  <div class="photo" role="img" aria-label="Photo of two women stretching on yoga mats" style="left:153px;top:815px;width:95px;height:86px;background:linear-gradient(180deg,#b89886,#dcc6b8 50%,#d08aaa)"></div>
  <div class="photo" role="img" aria-label="Photo of a woman meditating on a dock at sunrise" style="left:153px;top:909px;width:95px;height:64px;background:linear-gradient(180deg,#efc9a8,#ec9a66 50%,#7a4b34)"></div>
  <div class="photo" role="img" aria-label="Photo of a woman doing a shoulder stand on a dark background" style="left:255px;top:733px;width:95px;height:111px;background:linear-gradient(180deg,#3e3e3e,#2a2a2a)"></div>
  <div class="photo" role="img" aria-label="Photo of a handstand beside a brick wall in a gym" style="left:255px;top:853px;width:95px;height:120px;background:linear-gradient(180deg,#9a8a78,#5b544d 55%,#2f3235)"></div>

  <section class="abs testimonial" role="img" aria-label="Green tinted photo of misty hills and trees"></section>
  <div class="abs center label" style="top:1006px;color:#333">Testimonial</div>
  <h2 class="abs center title" style="top:1017px;color:#fff">Customer reviews</h2>
  <div class="abs quote-box"><p style="color:#fff;text-align:center;font-size:3.6px;line-height:6.2px">We all know that we need to reduce our exposure to toxins as much as possible. Today it is very hard to be completely clean and you'll probably never be able to achieve this. You just have to do the best you can. Environmental toxins can come in many forms.</p></div>
  <div class="abs avatar" role="img" aria-label="Client portrait"></div>
  <div class="abs center" style="top:1094px;font-size:3.8px;color:#333">Daniel Hart</div>
  <div class="abs" style="left:292px;top:1096px;display:flex;gap:1.5px"><span class="dot" style="background:#fff"></span><span class="dot" style="background:#fff"></span><span class="dot" style="background:#fff"></span></div>

  <section class="abs contact-sec" role="img" aria-label="Faint background photo of a table with a bowl of nuts"></section>
  <div class="abs center label" style="top:1154px">Contact Us</div>
  <div class="rule" style="top:1162px"></div>
  <h2 class="abs center title" style="top:1165px">Eat right for healthy</h2>
  <p class="abs center small" style="top:1180px;left:125px;width:150px">We all know that healthy eating is important. The Mediterranean style dietary principle and is sometimes</p>
  <form class="abs form">
    <div class="field" style="left:25px;top:16px;width:97px">First Name</div>
    <div class="field" style="left:130px;top:16px;width:97px">Last Name</div>
    <div class="field" style="left:25px;top:33px;width:97px">Email</div>
    <div class="field" style="left:130px;top:33px;width:97px">Phone Number</div>
    <div class="field" style="left:25px;top:50px;width:202px;padding-bottom:6px">Message</div>
    <div class="btn" style="left:104px;top:71px;width:44px;height:12px">Send Message</div>
  </form>

  <footer class="abs footer"></footer>
  <div class="abs foot-deco" role="img" aria-label="Faint photo of fresh carrots and herbs"></div>
  <h3 class="abs center" style="top:1364px;font-size:5.5px;font-weight:700">We Provide Best Services</h3>
  <p class="abs center small" style="top:1378px;left:125px;width:150px">We all know that healthy eating is important. The Mediterranean style dietary principle and is sometimes</p>
  <div class="abs center" style="top:1409px;display:flex;justify-content:center;align-items:center;gap:3px"><span class="dot" style="width:5px;height:5px"></span><span class="brand" style="font-size:10px">Verdant Fit</span></div>
  <div class="abs center" style="top:1431px;display:flex;justify-content:center;gap:6px;font-size:3.6px;color:#555;align-items:center">
    <span><svg width="4" height="5" viewBox="0 0 8 10"><path d="M4 10S0 5.5 0 3.5a4 4 0 018 0C8 5.5 4 10 4 10z" fill="#a3c429"/><circle cx="4" cy="3.5" r="1.4" fill="#fff"/></svg> 27 Meadow Lane Oakridge</span>
    <span><svg width="4" height="4" viewBox="0 0 10 10"><path d="M2 1l2 0 1 2-1 1.5c.6 1.2 1.3 1.9 2.5 2.5L8 5l2 1v2c-4.5 0-8-3.5-8-7z" fill="#a3c429"/></svg> +1 202-555-0147</span>
    <span><svg width="5" height="4" viewBox="0 0 10 8"><rect x="0.5" y="0.5" width="9" height="7" fill="none" stroke="#a3c429"/><path d="M.5 .5l4.5 4 4.5-4" fill="none" stroke="#a3c429"/></svg> hello@verdantfit.example</span>
  </div>
  <div class="badge" style="left:174px;width:18px"></div>
  <div class="badge" style="left:198px;width:26px;background:#334"></div>
  <div class="abs center" style="top:1469px;display:flex;justify-content:center;gap:3px"><span class="dot" style="background:#333"></span><span class="dot" style="background:#333"></span><span class="dot" style="background:#333"></span><span class="dot" style="background:#333"></span></div>
  <div class="abs center" style="top:1484px;font-size:3.6px;color:#555">@Copyright 2019</div>

</main>
</div>
</body>
</html>
```